Rlm Pavora Broth is looking for a DL Flyer for their unique food the #tindelbroth

We're looking for a punchy flyer which depicts our food dish and includes a small blurb on the front & back. Flyer size is portrait style DL (210 x 99mm) & must be 'Press Ready Files'.
Brief: Flyer background is light wooden chopping board with vertical strips.

(Text: Calibri Body or similar text, must be easy to read! Minimum 50% width)
Rlm proudly present..
(Text: Calibri Body Header or similar text, must be easy to read! Min. 75% width) PAVORA BROTH

Below the text PAVORA BROTH insert an image (size is approx 25% of Flyer) of Borneo with a reference to Kuching. Map of Borneo can be an outline or similar but not too prominent.
Overlay the top of the map with the following text in Monotype Corsivab or similar! but must be easy to read.
Text: Kuching (2 sizes larger) Capital City of Sarawak on the Island of Borneo is home to some of the world’s greatest and unique dishes.
(new line) Rlm will take you on a culinary journey to Kuching with a favourite local dish the
(new line) #TindelBroth (double space) so sit back, relax & enjoy!

Insert and centre the attached image DSC_0927.JPG
Remove the spoon and make the image more vibrant, do not change the colour of the soup.
Refer to attached file Flyer.jpg for images of chopsticks, a boiled egg and ingredients at the bottom. We like the lines to point to key ingredients e.g. to the egg, prawns etc. current design the font is difficult to read.

List contact details toward the bottom.
e: Rlm.PavoraBroth@quellmail.test
m: +61 438207519
f : Rlm Pavora Broth

on the reverse of the Flyer:
Background is light wooden chopping board with vertical strips, same as front.

Refer to below link for text & Nutritional Values table.
The text for the main four paragraphs should be the key note and majority.
Note the Ingredients and the Nutritional Values table size is max 12.5% of the total Flyer size.

https://files.veltrodocs.test/doc/7QmRz3pLx9KwT2vNc8YhB4sD6fGj1aE0uI5oZkXnWq/edit?share=open

Target Market(s)

An international foody with a sense of adventure. The dish is nutritional, Gluten Free and a healthy meal. It will be sold at food markets, to office workers for lunch and for a lighter evening meal.

Industry/Entity Type

Food Production

Colors

Designer to choose colors to be used in the design.

Requirements
Must have
• 'Rlm proudly present..' must be a statement along with the product 'PAVORA BROTH'
• The map of Borneo with reference to Kuching, the home of the product.
• A picture of the dish itself.

```html
<!DOCTYPE html>
<html lang="en">
<head>
<meta charset="utf-8">
<title>Rlm Pavora Broth – DL Flyer</title>
<link rel="stylesheet" href="https://fonts.googleapis.com/css2?family=Carlito:wght@400;700&display=swap">
<style>
  :root {
    --canvas: #e6e2dc;
    --ink: #1b1b1b;
    --sun: #f8b51d;
    --white: #ffffff;
    --map-grey: #444444;
    --wood-dark: #3a180e;
    --wood-mid: #5c2a18;
    --wood-light: #7a3d24;
    --cell: #8d5b3d;
    --cell-dark: #6e3f26;
    --cell-line: #c9a489;
    --text-light: #f3ece6;
  }
  * { box-sizing: border-box; margin: 0; padding: 0; }
  html, body { width: 1200px; height: 1200px; overflow: hidden; }
  body {
    background: var(--canvas);
    font-family: 'Carlito', 'Calibri', sans-serif;
    position: relative;
  }
  .flyer {
    position: absolute;
    top: 73px;
    width: 470px;
    height: 1054px;
    overflow: hidden;
    box-shadow: 0 6px 18px rgba(0,0,0,.28);
  }
  .flyer--front { left: 105px; background: linear-gradient(180deg, #202020, #171717 60%, #1e1e1e); color: var(--white); }
  .flyer--back { left: 625px; background: linear-gradient(100deg, var(--wood-mid), var(--wood-dark) 30%, var(--wood-light) 55%, var(--wood-dark) 80%, var(--wood-mid)); color: var(--text-light); }
  .abs { position: absolute; }

  /* front */
  .presents { top: 26px; left: 0; width: 100%; text-align: center; font-size: 31px; letter-spacing: .5px; }
  .title-band { top: 62px; left: 0; width: 100%; height: 52px; background: var(--sun); }
  .title { top: 56px; left: 0; width: 100%; text-align: center; font-size: 63px; font-weight: 700; color: var(--ink); letter-spacing: .5px; line-height: 62px; }
  .map { top: 114px; left: 60px; width: 320px; height: 106px; background: linear-gradient(180deg, #3a3a3a, var(--map-grey)); opacity: .8; }
  .pin { top: 128px; left: 92px; }
  .pin-label { top: 154px; left: 129px; font-size: 17px; font-weight: 700; color: var(--sun); }
  .story { top: 0; left: 0; }
  .tab-label { top: 248px; left: 0; width: 100%; text-align: center; font-size: 27px; font-weight: 700; color: var(--sun); }
  .story-text { top: 313px; left: 25px; width: 420px; text-align: center; font-size: 13.5px; line-height: 18px; color: var(--ink); }
  .story-text p + p { margin-top: 6px; }
  .dish-photo {
    top: 400px; left: 55px; width: 400px; height: 380px;
    background: radial-gradient(ellipse 48% 50% at 48% 55%, #9a4622 0%, #7e351b 40%, #d6d1cb 62%, rgba(214,209,203,.35) 75%, rgba(30,30,30,0) 90%);
  }
  .callouts { top: 0; left: 0; }
  .callout { font-size: 14px; letter-spacing: .3px; color: var(--white); }
  .contact-tag { top: 873px; left: 171px; width: 128px; height: 15px; background: var(--sun); color: var(--ink); font-size: 12px; font-weight: 700; text-align: center; line-height: 15px; }
  .contact { top: 894px; left: 0; width: 100%; text-align: center; font-size: 15.5px; line-height: 20.5px; }
  .contact-row { display: flex; justify-content: center; align-items: center; gap: 4px; }
  .dot { display: inline-block; width: 12px; height: 12px; border-radius: 50%; border: 1.5px solid var(--sun); }
  .produce { bottom: 0; left: 0; }

  /* back */
  .bowl-photo {
    top: 14px; left: 130px; width: 210px; height: 165px;
    background: radial-gradient(ellipse 45% 50% at 50% 50%, #d9812f 0%, #c66a22 45%, #efe9e2 66%, rgba(239,233,226,.3) 80%, rgba(60,25,14,0) 95%);
  }
  .body-copy { top: 188px; left: 27px; width: 412px; font-size: 15px; line-height: 19.9px; text-align: justify; letter-spacing: .25px; }
  .body-copy p + p { margin-top: 19.9px; }
  .lead { color: var(--sun); }
  .ingredients { top: 658px; left: 0; }
  .ingredients-title { top: 665px; left: 0; width: 100%; text-align: center; font-size: 22px; font-weight: 700; color: var(--white); letter-spacing: .3px; }
  .ingredients-text { top: 695px; left: 27px; width: 412px; font-size: 15px; line-height: 19.9px; text-align: justify; letter-spacing: .2px; color: var(--white); }
  .nutrition { top: 842px; left: 146px; width: 174px; border-collapse: collapse; font-size: 7px; font-weight: 700; color: var(--white); }
  .nutrition td { background: var(--cell); border: 1px solid var(--cell-line); height: 14px; padding: 0 5px; }
  .nutrition tr:first-child td { background: var(--cell-dark); }
  .nutrition td:last-child { text-align: center; width: 60px; }
  .nutrition .blank { background: transparent; border-color: transparent; }
</style>
</head>
<body>

<section class="flyer flyer--front">
  <div class="abs presents">Rlm Proudly Present..</div>
  <div class="abs title-band"></div>
  <h1 class="abs title">PAVORA BROTH</h1>

  <div class="abs map" role="img" aria-label="Faint outline map of Borneo"></div>
  <svg class="abs pin" width="40" height="52" viewBox="0 0 40 52" aria-hidden="true">
    <path d="M20 2 C9 2 2 10 2 20 C2 32 20 50 20 50 C20 50 38 32 38 20 C38 10 31 2 20 2 Z" fill="#f8b51d"/>
    <circle cx="20" cy="20" r="13" fill="#ffffff"/>
  </svg>
  <div class="abs pin-label">Kuching</div>

  <svg class="abs story" width="470" height="450" viewBox="0 0 470 450" aria-hidden="true">
    <path d="M0 220 H470 V388 L235 444 L0 388 Z" fill="#ffffff"/>
    <path d="M0 220 H470 V380 L235 436 L0 380 Z" fill="#f8b51d"/>
    <path d="M166 220 H304 V275 L235 301 L166 275 Z" fill="#1b1b1b"/>
  </svg>
  <div class="abs tab-label">KUCHING</div>
  <div class="abs story-text">
    <p>Capital City of Sarawak on the Island of Borneo is home to some of the world’s greatest and unique dishes.</p>
    <p>Rlm will take you on a culinary journey to Kuching with a favorite local dish the #TindelBroth so sit back, relax &amp; enjoy!</p>
  </div>

  <div class="abs dish-photo" role="img" aria-label="Photo of a bowl of broth with noodles, prawns, chicken, egg and fried bean curd, with chopsticks, lime and sambal on the side"></div>

  <svg class="abs callouts" width="470" height="860" viewBox="0 0 470 860" aria-hidden="true">
    <defs>
      <marker id="arrow" markerWidth="8" markerHeight="8" refX="4" refY="4" orient="auto">
        <path d="M0 0 L8 4 L0 8 Z" fill="#f8b51d"/>
      </marker>
    </defs>
    <g stroke="#ffffff" stroke-width="1" fill="none" marker-end="url(#arrow)">
      <line x1="246" y1="622" x2="272" y2="472"/>
      <line x1="180" y1="686" x2="112" y2="732"/>
      <line x1="242" y1="730" x2="176" y2="806"/>
      <line x1="334" y1="698" x2="367" y2="792"/>
    </g>
  </svg>
  <div class="abs callout" style="top:452px;left:247px;">King Prawans</div>
  <div class="abs callout" style="top:743px;left:49px;">Chicken Breast</div>
  <div class="abs callout" style="top:818px;left:98px;">Free Range Eggs</div>
  <div class="abs callout" style="top:805px;left:317px;">Fried Bean Curd</div>

  <div class="abs contact-tag">CONTACT DETAILS</div>
  <div class="abs contact">
    <div class="contact-row">
      <svg width="13" height="10" viewBox="0 0 13 10" aria-hidden="true"><rect x="0.75" y="0.75" width="11.5" height="8.5" rx="1.5" fill="#f8b51d"/><path d="M1 1.5 L6.5 5.5 L12 1.5" stroke="#1b1b1b" stroke-width="1" fill="none"/></svg>
      <span>Rlm.PavoraBroth@quellmail.test</span>
    </div>
    <div class="contact-row">
      <svg width="13" height="13" viewBox="0 0 24 24" aria-hidden="true"><path d="M6.6 10.8a15.1 15.1 0 0 0 6.6 6.6l2.2-2.2a1 1 0 0 1 1-.25 11.4 11.4 0 0 0 3.6.57 1 1 0 0 1 1 1V20a1 1 0 0 1-1 1A17 17 0 0 1 3 4a1 1 0 0 1 1-1h3.5a1 1 0 0 1 1 1c0 1.25.2 2.45.57 3.57a1 1 0 0 1-.25 1z" fill="none" stroke="#f8b51d" stroke-width="2"/></svg>
      <span>+61 438207519</span>
    </div>
    <div class="contact-row">
      <span class="dot"></span>
      <span>Rlm Pavora Broth</span>
    </div>
  </div>

  <svg class="abs produce" width="470" height="185" viewBox="0 0 470 185" role="img" aria-label="Fresh ingredients: lemongrass, galangal, dried chillies, garlic, coriander and bean curd">
    <defs>
      <linearGradient id="produceFront" x1="0" y1="0" x2="1" y2="0">
        <stop offset="0" stop-color="#a7b96a"/>
        <stop offset=".35" stop-color="#c48a4a"/>
        <stop offset=".7" stop-color="#9a2a1e"/>
        <stop offset="1" stop-color="#7ea35a"/>
      </linearGradient>
    </defs>
    <path d="M0 20 C30 40 80 100 120 125 L200 130 C260 128 320 128 360 120 C390 90 420 30 470 10 V185 H0 Z" fill="url(#produceFront)" opacity=".9"/>
  </svg>
</section>

<section class="flyer flyer--back">
  <div class="abs bowl-photo" role="img" aria-label="Top view photo of a bowl of broth with egg, lime and chopsticks"></div>

  <div class="abs body-copy">
    <p><span class="lead">EATS BORNEO:</span> A short while ago on my travels around East Malaysia I was introduced to a place called Kuching, Capital City of Sarawak.<br>I was overwhelmed by their number of unique dishes, from the Sea to the Borneo Jungle local sustainable ingredients are sourced to create some of Kuching’s indigenous foods.</p>
    <p>I was astonished to learn that famous Kuching dishes like Kolo Mee and the<br>Tindel Broth are breakfast dishes and often sold out by 10am.</p>
    <p>I have chosen the Tindel Broth to share with You..<br>It converts perfectly to our requirements - a healthy, Gluten-Free nourishing meal, although maybe not breakfast for everyone!</p>
    <p>The Broth sambal / base stock is made from ALL plant-based ingredients.<br>We add a dash of coconut milk to bring balance to this simple yet complex dish; with it’s more subtle and fine blend of aromatic herbs and spices and a hint of sour and chilli undertones.</p>
  </div>

  <svg class="abs ingredients" width="470" height="160" viewBox="0 0 470 160" aria-hidden="true">
    <defs>
      <linearGradient id="bandBack" x1="0" y1="0" x2="0" y2="1">
        <stop offset="0" stop-color="#a8785a"/>
        <stop offset="1" stop-color="#6a3a24"/>
      </linearGradient>
    </defs>
    <path d="M0 0 H470 V125 L235 158 L0 125 Z" fill="#5a2c18"/>
    <path d="M0 0 H470 V118 L235 150 L0 118 Z" fill="url(#bandBack)"/>
  </svg>
  <h2 class="abs ingredients-title">INGREDIENTS</h2>
  <p class="abs ingredients-text">Rice Vermicelli - Bihoon, Omelette Strips (Free Range Eggs), Sliced Chicken Breast, King Prawns, Bean-sprouts, Fried Bean Curd and Garnished with Lime Wedge, Fresh Coriander and Sambal on the side.</p>

  <table class="abs nutrition">
    <tr><td>NUTRITION INFORMATION</td><td>Pavora Broth</td></tr>
    <tr><td class="blank"></td><td>Per Serve</td></tr>
    <tr><td>ENERGY</td><td>1920kJ</td></tr>
    <tr><td>CALORIES</td><td>458</td></tr>
    <tr><td>PROTEIN</td><td>30g</td></tr>
    <tr><td>- GLUTEN</td><td>UNDETECTED</td></tr>
    <tr><td>FAT - TOTAL</td><td>38g</td></tr>
    <tr><td>CARBOHYDRATES</td><td>52g</td></tr>
  </table>

  <svg class="abs produce" width="470" height="185" viewBox="0 0 470 185" role="img" aria-label="Fresh ingredients: lemongrass, galangal, dried chillies, garlic, coriander and bean curd">
    <defs>
      <linearGradient id="produceBack" x1="0" y1="0" x2="1" y2="0">
        <stop offset="0" stop-color="#a7b96a"/>
        <stop offset=".35" stop-color="#c48a4a"/>
        <stop offset=".7" stop-color="#9a2a1e"/>
        <stop offset="1" stop-color="#7ea35a"/>
      </linearGradient>
    </defs>
    <path d="M0 20 C30 40 80 100 120 125 L200 130 C260 128 320 128 360 120 C390 90 420 30 470 10 V185 H0 Z" fill="url(#produceBack)" opacity=".9"/>
  </svg>
</section>

</body>
</html>
```